Flyer design for retail store owners

i would need to have a flyer design for my retail shop customers to show that I am a mailbox store that has all major shipping vendors to for their shipping needs. Ensuring that they can take advantage of opening a house account at the store and billed monthly, word document has all the details. Please use stock images for the notary public, passport photos, mailbox brass pictures of my actual mailboxes are listed in the pictures. I need to make it POP and WOW these retail store owners as I am using it to advertise the business

```html
<!DOCTYPE html>
<html lang="en">
<head>
<meta charset="utf-8">
<title>Mailbox Rental &amp; Pack and Ship Flyer</title>
<link href="https://fonts.googleapis.com/css2?family=Anton&family=Arimo:wght@400;700&display=swap" rel="stylesheet">
<style>
  :root{
    --backdrop:#a6a6a6;
    --paper:#ffffff;
    --tan:#c68f53;
    --peach:#fec689;
    --panel:#ececec;
    --ink:#111111;
    --body:#1e1e1e;
  }
  *{box-sizing:border-box;margin:0;padding:0}
  html,body{width:1200px;height:1200px;overflow:hidden}
  body{background:var(--backdrop);position:relative;font-family:"Arimo",Arial,sans-serif;color:var(--body)}
  .page{position:absolute;top:260px;width:466px;height:657px;background:var(--paper);overflow:hidden}
  .page--rent{left:102px}
  .page--ship{left:629px}
  .abs{position:absolute}
  .display{font-family:"Anton",Impact,sans-serif;font-weight:400;letter-spacing:-0.5px;line-height:1;text-transform:uppercase}
  .copy{font-size:8.6px;line-height:12.2px;text-align:justify}
  .photo{position:absolute}

  /* renting page */
  .corner-shape{position:absolute;left:0;top:0}
  .side-bar{left:0;top:24px;width:19px;height:103px;background:var(--tan)}
  .title-main{left:35px;top:20px;font-size:61px;color:var(--ink)}
  .title-sub{left:35px;top:78px;font-size:45px;color:var(--tan)}
  .rent-intro{left:36px;top:129px;width:202px}
  .mailbox-unit{left:255px;top:39px;width:195px;height:222px;background:linear-gradient(135deg,#e0b884,#b98a53 60%,#8f6537)}
  .promo-band{left:0;top:297px;width:466px;height:147px;background:var(--peach)}
  .tag{position:absolute;background:var(--tan);color:#fff;font-weight:700;font-size:11px;line-height:25px;padding:0 6px;text-transform:uppercase}
  .tag--promo{left:34px;top:297px;width:116px}
  .promo-copy{left:36px;top:329px;width:204px}
  .signing-frame{left:260px;top:282px;width:185px;height:137px;background:var(--paper)}
  .signing-photo{left:268px;top:283px;width:171px;height:130px;background:linear-gradient(160deg,#f2f2f2,#cfcfcf 45%,#2b2b2b 70%,#111)}
  .tag--deals{left:34px;top:444px;width:206px;height:25px}
  .deals-panel{left:240px;top:444px;width:226px;height:148px;background:var(--panel)}
  .deal-list{list-style:none;position:absolute;font-size:8.6px;line-height:12.2px}
  .deal-list li{position:relative;padding-left:0;margin-bottom:8px}
  .deal-list li::before{content:"";position:absolute;left:-13px;top:3px;width:6px;height:6px;border-radius:50%;background:var(--tan)}
  .deal-list--left{left:48px;top:487px;width:175px}
  .deal-list--right{left:263px;top:486px;width:172px}
  .deal-list--right li{margin-bottom:11px;text-align:justify}
  .footer-band{left:0;width:466px;background:var(--tan)}
  .page--rent .footer-band{top:621px;height:36px;color:#fff;font-weight:700;font-size:13px;line-height:36px;text-align:center}

  /* shipping page */
  .kicker{left:28px;top:49px;font-size:29px;color:var(--tan)}
  .title-ship{left:27px;top:78px;font-size:47px;color:var(--ink)}
  .lede{left:28px;top:126px;width:235px;font-size:12.6px;line-height:16px}
  .ship-band{left:0;top:171px;width:466px;height:105px;background:var(--peach)}
  .door-frame{left:262px;top:22px;width:177px;height:167px;background:var(--paper)}
  .door-photo{left:269px;top:23px;width:162px;height:159px;background:linear-gradient(135deg,#caa05c,#b08444 55%,#6e4f24)}
  .ship-copy{left:28px;top:206px;width:411px;font-size:8.6px;line-height:12.2px}
  .slot-photo{left:28px;top:296px;width:196px;height:111px;background:linear-gradient(180deg,#5c5f66,#6c7078 50%,#53565d)}
  .passport-a{left:244px;top:296px;width:190px;height:109px;background:linear-gradient(180deg,#e6e3e0,#cdbfb4)}
  .passport-b{left:28px;top:429px;width:194px;height:107px;background:linear-gradient(180deg,#dfe2e8,#bfc4cf)}
  .garden-photo{left:242px;top:426px;width:195px;height:111px;background:linear-gradient(90deg,#4f6b45,#d8663f 35%,#e0cf3f 55%,#4da5c6 75%,#b7a893)}
  .partners-line{left:0;top:556px;width:466px;text-align:center;font-weight:700;font-size:13px;color:var(--tan)}
  .partner{position:absolute;top:594px;font-weight:700;font-size:11px;color:var(--ink);white-space:nowrap;transform:translateX(-50%)}
  .page--ship .footer-band{top:643px;height:14px}
</style>
</head>
<body>

<section class="page page--rent">
  <svg class="corner-shape" width="466" height="120" viewBox="0 0 466 120" aria-hidden="true">
    <polygon points="297,0 466,0 466,115" fill="var(--peach)"/>
  </svg>
  <div class="abs side-bar"></div>
  <h1 class="abs display title-main">Renting</h1>
  <h2 class="abs display title-sub">A Mail Box</h2>
  <p class="abs copy rent-intro">is one of the most efficient and cost saving methods for receiving your mail and packages. Instead of having to worry about private security, weather conditions, sorting, and deliveries; all you have to do is pick-up your mail from our secured facility each day except Sundays. You will get a notification when mail arrives whether envelope or package, it will be scanned in daily which other mailbox stores do not offer! We offer onsite Notary Public with no appointments and onsite Passport Photos and can ship out same day.</p>
  <div class="photo mailbox-unit" role="img" aria-label="Photo of a brass mailbox cabinet with rows of small locking doors"></div>

  <div class="abs promo-band"></div>
  <div class="tag tag--promo">Main Promotion:</div>
  <p class="abs copy promo-copy">Now renting mailboxes on Maple Ridge Crossing Shopping Center. We are offering all Maple Ridge crossing shopping center owners/employees an exclusive promo deal! $12 a month for 6-12 months leases! You get a mailbox in the shop, a book of stamps(20 count), 3 notarizations by appointment, 100 copies of black and white, and 100 copies of color. Please see associate for sign up!</p>
  <div class="abs signing-frame"></div>
  <div class="photo signing-photo" role="img" aria-label="Photo of hands signing a document at a desk with a notary stamp"></div>

  <div class="abs deals-panel"></div>
  <div class="tag tag--deals">Check out these other deals!</div>
  <ul class="deal-list deal-list--left">
    <li>As a retail owner, you know how important it is to keep your customers coming back - you will get 20% discount for printing services.</li>
    <li>We duplicate keys for $2/each, our regular price charge is $4/each. Save up to 50%!</li>
    <li>Lamination is also discounted at 10% off.</li>
  </ul>
  <ul class="deal-list deal-list--right">
    <li>10% off retail supplies ... must be minimum of 10$</li>
    <li>For house accounts -a 5% discount will be deducted monthly of billing change to invoicing PLUS we're giving another 5% of the discount if you upgrade and sign up for mailbox. Great right?</li>
  </ul>

  <div class="abs footer-band">Take advantage of this limited time offer now!</div>
</section>

<section class="page page--ship">
  <p class="abs display kicker">At Swift Parcel</p>
  <h1 class="abs display title-ship">Pack &amp; Ship</h1>
  <p class="abs lede">our goal is to make your shipping experience as convenient as possible.</p>
  <div class="abs ship-band"></div>
  <div class="abs door-frame"></div>
  <div class="photo door-photo" role="img" aria-label="Close-up photo of an open brass mailbox door with padlock"></div>
  <p class="abs ship-copy">Whether you are shipping packages, documents, or packages, we are here to help. Whether you want to track your package or estimate the price of your package, it is easy for you. We are ready to handle all of your postal services! Get also the services you need; printing, copying, and stop in to purchase postage or shipping materials.</p>

  <div class="photo slot-photo" role="img" aria-label="Photo of a brass letter slot on a grey front door"></div>
  <div class="photo passport-a" role="img" aria-label="Sheet of passport photos"></div>
  <div class="photo passport-b" role="img" aria-label="Sheet of passport photos"></div>
  <div class="photo garden-photo" role="img" aria-label="Photo of a rainbow striped mailbox beside a wooden fence"></div>

  <p class="abs partners-line">Service point partners are Parcelon, Unibox, Stateline Post, and Dash Freight.</p>
  <span class="partner" style="left:100px">Parcelon</span>
  <span class="partner" style="left:167px">Unibox</span>
  <span class="partner" style="left:257px">Stateline Post</span>
  <span class="partner" style="left:362px">Dash Freight</span>

  <div class="abs footer-band"></div>
</section>

</body>
</html>
```